Pflegedienst sucht Flyerdesign
Zielgruppe
Wir sind ein ambulanter Pflegedienst und betreuen ca. 200 Patienten in ländlicher Region. Unsere Zielgruppe sind Pflegebedürftige aus altersbedingten Gründen oder nach Krankenhausaufenthalten. Wir setzen auf Qualität, Zuverlässigkeit, Exklusivität.
Aufgabenstellung
DIN lang Flyer. Wir werben ganz bewußt nicht mit Bildern von Senioren oder alten Menschen, weil das fast alle Pflegedienste tun. Daher setzen wir eher auf Motive aus unserer Urlaubsregion: Strand, Meer...
Unseren Firmen-Vebo hätten wir gern als Fotoausschnitt ohne Hintergund mit dabei.
Und einen Kartenausschnitt mit unserem Einzugsgebiet fänden wir toll. Dies umfasst ca. 15 km um Laboe und Heikendorf folgende Orte: Stein, Wendtorf, Probsteierhagen, Schönkirchen und Mönkeberg.

```html
<!DOCTYPE html>
<html lang="de">
<head>
<meta charset="utf-8">
<title>Flyer DIN lang – Pflegeteam Strandhagen</title>
<link rel="stylesheet" href="https://fonts.googleapis.com/css2?family=Barlow+Condensed:wght@500&family=Open+Sans:ital,wght@0,400;0,600;0,700;1,400;1,600&display=swap">
<style>
:root{
  --magenta:#a3195f;
  --magenta-dark:#7d1248;
  --magenta-light:#c44d8a;
  --grey-panel:#ebecee;
  --grey-text:#7d858c;
  --dark-text:#3a3a3a;
  --rule:#c8d08a;
  --white:#ffffff;
}
*{margin:0;padding:0;box-sizing:border-box}
html,body{width:896px;height:1200px;overflow:hidden;background:var(--white)}
body{position:relative;font-family:"Open Sans",Arial,sans-serif;color:var(--dark-text)}
.spread{position:absolute;width:677px;height:478px;overflow:hidden;background:var(--white);box-shadow:0 0 4px rgba(0,0,0,.25)}
.spread--outside{left:20px;top:34px}
.spread--inside{left:184px;top:492px}
.spread-bg{position:absolute;left:0;top:0}
.abs{position:absolute}
.fold{position:absolute;top:0;width:1px;height:100%;background:var(--rule);opacity:.7}
.brand{position:absolute;font-family:"Open Sans",Arial,sans-serif;font-weight:600;color:var(--grey-text);white-space:nowrap;line-height:1}
.brand--small{font-size:8px}
.brand--mid{font-size:9px}
.brand--large{right:47px;top:1072px;font-size:18px}
.hero-title{left:27px;top:160px;color:var(--white);font-family:"Barlow Condensed",Arial,sans-serif;font-weight:500;font-size:21px;line-height:23px}
.hero-sub{left:27px;top:250px;color:var(--white);font-weight:700;font-size:10px;line-height:15px}
.hero-tag{left:50px;top:358px;background:rgba(255,255,255,.35);color:var(--white);font-size:8px;font-weight:600;padding:2px 4px}
.contact{left:275px;width:170px;font-size:7px;line-height:9.5px;color:var(--grey-text)}
.contact strong{color:var(--dark-text);font-weight:600}
.contact .hot{color:var(--magenta);font-weight:700;font-size:9.5px;line-height:12px}
.contact .co{color:var(--magenta);font-weight:700;font-size:8px}
.partners-h{left:244px;top:332px;font-size:6.5px;color:var(--magenta);font-weight:600}
.person{position:absolute;top:345px;width:66px;font-size:5.6px;line-height:7px;color:var(--grey-text)}
.person .photo{width:46px;height:46px;margin-bottom:4px;background:linear-gradient(160deg,#d9c3b4,#8a6d5f)}
.person b{color:var(--dark-text);font-weight:700;display:block}
.claim{left:502px;top:115px;color:var(--magenta);font-weight:600;font-size:15.5px;line-height:20px}
.claim-sub{left:502px;top:159px;font-size:8.5px;line-height:11.5px;font-weight:600;color:#555}
.services{left:502px;top:360px;font-size:6.4px;line-height:11px;color:var(--magenta-light);list-style:none}
.intro-h{left:37px;top:113px;width:180px;color:var(--white);font-family:"Barlow Condensed",Arial,sans-serif;font-weight:500;font-size:12px;line-height:13px}
.intro{left:37px;top:176px;width:178px;color:var(--white);font-size:7.2px;line-height:12.5px}
.intro p+p{margin-top:10px}
.callus{left:37px;top:408px;color:var(--white);font-size:8px;font-weight:700;line-height:12px}
.callus span{font-size:10.5px}
.tasks{left:252px;top:112px;width:196px;font-size:6px;line-height:8.6px}
.tasks .h{color:var(--magenta);font-weight:700;margin-bottom:8px}
.tasks .it{font-style:italic;padding-left:14px;margin-bottom:3px}
.tasks .sub{font-weight:700;margin-top:8px}
.tasks ul{list-style:none;padding-left:8px}
.tasks li{position:relative}
.tasks li::before{content:"+";position:absolute;left:-8px;color:var(--magenta);font-weight:700}
.team{left:481px;top:112px;font-size:6.4px;line-height:11px}
.team .h{font-weight:700;line-height:8.5px;margin-bottom:6px}
.team ul{list-style:none;color:var(--magenta)}
.team li::before{content:"› ";color:var(--grey-text)}
.strengths-h{left:481px;top:267px;font-size:6.4px;font-weight:700}
.strength{position:absolute;font-size:6.2px;line-height:8px;font-style:italic;font-weight:600;color:var(--magenta)}
.caption{left:185px;top:1036px;color:var(--magenta);font-size:13px;line-height:20px}
</style>
</head>
<body>

<section class="spread spread--outside">
  <svg class="spread-bg" width="677" height="478" viewBox="0 0 677 478">
    <defs>
      <linearGradient id="heroFill" x1="0" y1="0" x2="1" y2="1">
        <stop offset="0" stop-color="#b03172"/>
        <stop offset="1" stop-color="#6e0f40"/>
      </linearGradient>
    </defs>
    <path d="M222 0H677V478H222Z" fill="#f5f5f6"/>
    <path d="M222 110 Q334 92 446 110 L446 478 H222Z" fill="var(--grey-panel)"/>
    <path d="M446 110 Q560 82 677 100 V478 H446Z" fill="var(--grey-panel)"/>
    <path d="M0 108 Q111 88 222 92 V478 H0Z" fill="url(#heroFill)" role="img" aria-label="Strandfoto der Küste mit Kartenausschnitt des Einzugsgebiets"/>
    <circle cx="600" cy="280" r="95" fill="var(--magenta)"/>
    <circle cx="625" cy="366" r="39" fill="#9aa3ab" stroke="#fff" stroke-width="2" role="img" aria-label="Foto des Firmenwagens"/>
    <circle cx="288" cy="83" r="18" fill="#fff" stroke="#d8d8d8"/>
    <path d="M281 76c2-2 3-1 4 1l1 3c0 1-1 2-2 2 1 3 3 5 6 6 0-1 1-2 2-2l3 1c2 1 3 2 1 4-2 2-5 2-9-1-4-3-7-7-7-10 0-2 0-3 1-4z" fill="var(--magenta)"/>
  </svg>
  <div class="fold" style="left:222px"></div>
  <div class="fold" style="left:446px"></div>

  <div class="brand brand--small" style="right:466px;top:50px">PFLEGETEAM STRANDHAGEN</div>
  <div class="abs hero-title">WÜRDE<br>LEBENSQUALITÄT<br>SELBSTBESTIMMUNG</div>
  <div class="abs hero-sub">von Mensch zu Mensch<br>seit über 20 Jahren</div>
  <div class="abs hero-tag">Für Sie vor Ort</div>

  <div class="abs contact" style="top:115px">
    <div class="hot">Rufbereitschaft:<br>0170 – 28 36 415</div>
    <div class="co" style="margin-top:13px">Pflegeteam Strandhagen GmbH</div>
    <strong>Hauptsitz:</strong><br>Lindenweg 7<br>23411 Strandhagen<br>TEL 04512 – 27 90<br>FAX 04512 – 27 91
    <div style="margin-top:12px">info@pflegeteam-strandhagen.de<br>www.pflegeteam-strandhagen.de</div>
    <div style="margin-top:12px"><strong>Niederlassung:</strong><br>Mühlenstraße 4<br>23418 Kliffhusen<br>TEL 04513 - 24 17 53 60<br>FAX 04513 - 24 17 53 61</div>
  </div>
  <div class="abs partners-h">Ihre Ansprechpartner:</div>
  <div class="person" style="left:244px"><div class="photo" role="img" aria-label="Porträtfoto Sabine Hartwig"></div><b>Sabine Hartwig</b>Geschäftsleitung</div>
  <div class="person" style="left:310px"><div class="photo" role="img" aria-label="Porträtfoto Anna Petersen"></div><b>Anna Petersen</b>Pflegedienstleitung<br><br>Einsatzleitung<br>Kliffhusen</div>
  <div class="person" style="left:376px"><div class="photo" role="img" aria-label="Porträtfoto Maren Lohse"></div><b>Maren Lohse</b>Stellv. Pflege-<br>dienstleitung<br><br>Einsatzleitung<br>Strandhagen</div>

  <div class="brand brand--mid" style="right:22px;top:42px">PFLEGETEAM STRANDHAGEN</div>
  <div class="abs claim">Ihr Premiumdienst<br>in der Region</div>
  <div class="abs claim-sub">von Mensch zu Mensch<br>seit über 20 Jahren</div>
  <ul class="abs services">
    <li>Häusliche Pflege</li><li>Pflegeberatung</li><li>Demenzbetreuung</li><li>Aktivierende Beschäftigung</li><li>Entlastung im Haushalt</li><li>Palliativpflege Sterbebegleitung</li><li>24 h Rufbereitschaft</li>
  </ul>
</section>

<section class="spread spread--inside">
  <svg class="spread-bg" width="677" height="478" viewBox="0 0 677 478">
    <defs>
      <linearGradient id="seaFill" x1="0" y1="0" x2="0" y2="1">
        <stop offset="0" stop-color="#9c1d5e"/>
        <stop offset="1" stop-color="#b4497e"/>
      </linearGradient>
    </defs>
    <path d="M229 0H677V478H229Z" fill="#f5f5f6"/>
    <path d="M229 62 Q343 38 457 52 V478 H229Z" fill="var(--grey-panel)"/>
    <path d="M457 52 Q567 34 677 44 V478 H457Z" fill="var(--grey-panel)"/>
    <path d="M0 70 Q114 44 229 62 V478 H0Z" fill="url(#seaFill)" role="img" aria-label="Foto einer Meeresbucht mit Strand, magentafarben eingefärbt"/>
    <line x1="23" y1="4" x2="23" y2="66" stroke="#bbb" stroke-dasharray="2 2"/>
    <circle cx="690" cy="372" r="95" fill="var(--magenta)"/>
    <circle cx="690" cy="372" r="170" fill="none" stroke="#c9cdd1" stroke-width="2" stroke-dasharray="1 6" stroke-linecap="round"/>
  </svg>
  <div class="fold" style="left:229px"></div>
  <div class="fold" style="left:457px"></div>

  <div class="abs intro-h">EINEN AMBULANTEN PFLEGEDIENST IN ANSPRUCH ZU NEHMEN, BEDEUTET VERTRAUEN ZU SCHAFFEN.</div>
  <div class="abs intro">
    <p>Deswegen möchten wir uns bei einem Erstgespräch vorstellen und uns gegenseitig kennen lernen. Dabei entwickeln wir mit Ihnen, Ihren Angehörigen und unseren Pflegekräften ein auf Sie abgestimmtes individuelles Versorgungskonzept und beraten Sie natürlich gerne auch zur Finanzierung.</p>
    <p>Im Mittelpunkt unserer Bemühungen stehen die Zufriedenheit und die Lebensqualität unserer Patienten. Deswegen begreifen wir unsere Arbeit als einen ständigen Prozess, innerhalb dessen wir die individuelle Situation der Pflegebedürftigen ständig überprüfen, um ihnen die jeweils bestmögliche und auf ihre Bedürfnisse optimal abgestimmte Pflegequalität zukommen lassen zu können.</p>
  </div>
  <div class="abs callus">Rufen Sie uns gerne an:<br><span>04512 - 2790</span></div>

  <div class="abs tasks">
    <div class="h" style="padding-left:14px">Als Vertragspartner aller Kranken- und Pflegekassen helfen wir, wo wir können:</div>
    <div class="it">bei Pflegebedürftigkeit</div>
    <div class="it">bei Krankheit oder nach Entbindungen</div>
    <div class="it">bei Behinderung und Einschränkungen im Alltag besonders bei Demenz</div>
    <div class="it">nach Krankenhausaufenthalten oder ambulanten Operationen</div>
    <div class="it">bei Verhinderung der privaten Pflegepersonen in der letzten Lebensphase zu Hause</div>
    <div class="it">bei Urlaub mit Pflegebedürftigkeit in unserer Region</div>
    <div class="h" style="margin-top:8px;margin-bottom:0">Und kümmern uns je nach Bedarf mehrmals täglich um Sie:</div>
    <div class="sub">Im Rahmen ärztlicher Verordnungen</div>
    <ul><li>versorgen wir Wunden und wechseln Verbände</li><li>verabreichen wir Injektionen</li><li>stellen wir Medikamente und überwachen die Einnahme</li><li>ziehen wir Kompressionsstrümpfe an und aus</li><li>messen wir Blutdruck und Blutzucker</li></ul>
    <div class="sub">Im Rahmen der Pflegekasse</div>
    <ul><li>helfen wir bei der täglichen Körperpflege oder leiten Sie an</li><li>beobachten wir umfassend Ihren Allgemeinzustand</li><li>machen Bewegungsübungen, Spaziergänge oder begleiten Sie zum Arzt oder Aktivitäten</li><li>bereiten wir Ihnen Essen zu und kaufen ein</li><li>unterstützen wir bei der hauswirtschaftlichen Versorgung</li><li>betreuen und entlasten wir Sie</li></ul>
    <div class="sub">Oder wir vermitteln Ihnen Leistungen unserer langjährigen Kooperationspartner</div>
    <ul style="margin-top:6px"><li>Pflegehilfsmittel, Essen auf Rädern, Krankentransporte, Fußpflege, Hausnotruf, etc.</li></ul>
  </div>

  <div class="brand brand--mid" style="right:22px;top:42px">PFLEGETEAM STRANDHAGEN</div>
  <div class="abs team">
    <div class="h">Unser motiviertes und freundliches<br>Team besteht aus:</div>
    <ul><li>Examinierten Pflegefach- &amp; Führungskräften</li><li>Palliativfachkräften</li><li>Wundmanagern</li><li>Hygienefachkräften</li><li>Pflegeberatern</li><li>Haus- &amp; Familienpfleger/innen</li><li>Betreuungskräften &amp; Beschäftigungsassistenten</li><li>Hauswirtschaftler/innen</li><li>Kaufmännischen Verwaltungskräften</li></ul>
  </div>
  <div class="abs strengths-h">Unser Stärken:</div>
  <div class="strength" style="left:564px;top:270px">sehr gute, MDK-geprüfte<br>Pflegequalität</div>
  <div class="strength" style="left:509px;top:306px">Ehrlichkeit, Transparenz,<br>Fairness</div>
  <div class="strength" style="left:478px;top:342px">individuelle Rundumversorgung<br>und partnerschaftlicher Umgang</div>
  <div class="strength" style="left:483px;top:378px">inhabergeführtes Unternehmen<br>mit schlanken Strukturen<br>und über 20 Jahren Erfahrung</div>
  <div class="strength" style="left:496px;top:420px">angenehmes, familiäres<br>Arbeitsklima</div>
</section>

<div class="abs caption">Flyer Lang DIN<br>Wickelfalz</div>
<div class="brand brand--large">PFLEGETEAM STRANDHAGEN</div>

</body>
</html>
```